Fast Food (Pie Restaurant) Packaging Concept and Design

Please see attached a Concept Page with packaging items for our new Fast Food Pie Restaurant - including:
> Adult Clam - For Meat Pie, Mash, Peas and Gravy
> Kids Box - For Mini Meat Pie, Chips and a Cookie
> Large Chip Packet
> Takeaway Container - For Veg or Mash or Gravy
> Brown Paper Bag - For Cookies or Pies
> Plastic Pie Wrapper
> Napkins
Please submit an A4 page with all packaging items, showing your design concept. Use of up to 2 colours only except the kids box - you can use more colours. The winner will be asked to put these designs onto the templates for each packaging item for print.
I have also attached our logo and a page of packaging designs that I like to give you some ideas.
Crumb Tart Hut is a fast food pie restaurant. It's menu is mainly the sale of different kinds of meat pies with a choice of mash potato (different flavours), a vegetable (range of flavours) and a sauce or gravy. We also sell Chips with Rosemary Salt and Cookies. The Packaging design we like are those with patterns or fun ones with lots of words (of course pie related).
Info or words you can add to the packaging:
- 100% PNG Owned and Made
- Hamamas (means happy in our local language)
- Good Kai (means good food)
- I GAT TRUPLA FLAVA (it has lots of flavour)
- www.crumbtarthut.com.pg (yet to be created)
- Graphics of Peas, Pies (oval), Potatoes, Gravy ect.
- Tenk you long sapotim mipela! (thanks for supporting us)
Updates
Target Market(s)
Families and University Students
Look and feel
Each slider illustrates characteristics of the customer's brand and the style your logo design should communicate.

```html
<!DOCTYPE html>
<html lang="en">
<head>
<meta charset="utf-8">
<title>Crumb Tart Hut – Adult Clam Packaging</title>
<link rel="stylesheet" href="https://fonts.googleapis.com/css2?family=Arimo:wght@400;700&family=Cabin+Sketch:wght@400;700&display=swap">
<style>
  :root {
    --paper: #ffffff;
    --kraft: #bf8f6a;
    --kraft-dark: #8a5a3a;
    --fold-line: #4a3426;
    --ink: #231f20;
    --leaf: #68ab29;
    --crust: #e9dccb;
    --crust-edge: #b49a7c;
    --caption: #7a7a7a;
    --chalk: #ffffff;
  }
  html, body {
    margin: 0;
    padding: 0;
    width: 1200px;
    height: 848px;
    overflow: hidden;
    background: var(--paper);
  }
  .dieline {
    display: block;
    width: 1200px;
    height: 848px;
  }
  .kraft { fill: var(--kraft); }
  .kraft-shade { fill: var(--kraft-dark); }
  .fold { fill: none; stroke: var(--fold-line); stroke-width: 1; stroke-linejoin: round; }
  .side-badge { fill: var(--ink); }
  .brand-blob { fill: var(--paper); }
  .stripe { fill: var(--leaf); }
  .pie-art { fill: var(--crust); stroke: var(--crust-edge); stroke-width: 1; }
  .thanks {
    font-family: "Arimo", Arial, sans-serif;
    font-weight: 700;
    font-size: 17px;
    fill: var(--ink);
  }
  .origin-small {
    font-family: "Arimo", Arial, sans-serif;
    font-size: 10.5px;
    fill: var(--ink);
  }
  .origin-side {
    font-family: "Arimo", Arial, sans-serif;
    font-size: 14px;
    fill: var(--chalk);
  }
  .brand-name {
    font-family: "Arimo", Arial, sans-serif;
    font-weight: 700;
    font-size: 29px;
    fill: var(--leaf);
  }
  .brand-tagline {
    font-family: "Arimo", Arial, sans-serif;
    font-weight: 700;
    font-size: 9.5px;
    fill: var(--ink);
  }
  .chalk-word {
    font-family: "Cabin Sketch", "Comic Sans MS", cursive;
    fill: var(--chalk);
  }
  .good-kai { font-size: 27px; }
  .hamamas { font-size: 38px; }
  .item-caption {
    font-family: "Arimo", Arial, sans-serif;
    font-weight: 700;
    font-size: 12.5px;
    fill: var(--caption);
  }
</style>
</head>
<body>
<svg class="dieline" viewBox="0 0 850 600" preserveAspectRatio="none" xmlns="http://www.w3.org/2000/svg">

  <g class="box-net">
    <polygon class="kraft" points="148,60 692,60 655,146 182,146"/>
    <polygon class="kraft" points="182,432 655,432 692,517 148,517"/>
    <rect class="kraft" x="182" y="146" width="473" height="286"/>
    <polygon class="kraft" points="148,60 97,78 97,497 148,517 182,432 182,146"/>
    <polygon class="kraft" points="692,60 740,78 740,497 692,517 655,432 655,146"/>

    <polygon class="kraft-shade" points="97,80 148,60 182,146 97,112"/>
    <polygon class="kraft-shade" points="97,466 182,432 148,517 97,497"/>
    <polygon class="kraft-shade" points="740,80 692,60 655,146 740,112"/>
    <polygon class="kraft-shade" points="740,466 655,432 692,517 740,497"/>
  </g>

  <path class="side-badge" d="M97,178 C130,165 168,175 175,215 C182,265 165,300 175,345 C182,385 150,410 97,402 Z"/>
  <path class="side-badge" d="M740,170 C715,168 690,185 688,225 C685,270 700,300 690,345 C682,385 705,408 740,402 Z"/>

  <path class="brand-blob" d="M330,200 C380,188 470,190 520,200 C556,210 560,250 545,285 C532,320 548,360 520,385 C490,410 430,400 380,395 C330,390 295,360 280,325 C265,290 275,212 330,200 Z"/>
  <rect class="stripe" x="366" y="146" width="112" height="89"/>
  <rect class="stripe" x="366" y="342" width="116" height="175"/>

  <circle class="pie-art" cx="370" cy="148" r="21" role="img" aria-label="Sketched lattice-top pie"/>
  <circle class="pie-art" cx="462" cy="423" r="30" role="img" aria-label="Sketched lattice-top pie"/>

  <text class="brand-name" x="419" y="293" text-anchor="middle">Crumb Tart Hut</text>
  <text class="brand-tagline" x="419" y="322" text-anchor="middle" textLength="214" lengthAdjust="spacing">FAST FOOD PIE RESTAURANT</text>

  <g class="fold-lines">
    <polygon class="fold" points="148,60 692,60 740,78 740,497 692,517 148,517 97,497 97,78"/>
    <rect class="fold" x="182" y="146" width="473" height="286"/>
    <line class="fold" x1="148" y1="60" x2="182" y2="146"/>
    <line class="fold" x1="692" y1="60" x2="655" y2="146"/>
    <line class="fold" x1="148" y1="517" x2="182" y2="432"/>
    <line class="fold" x1="692" y1="517" x2="655" y2="432"/>
  </g>

  <g transform="rotate(180 420 100)">
    <text class="thanks" x="420" y="96" text-anchor="middle">Tenk you long sapotim mipela!</text>
    <text class="origin-small" x="420" y="114" text-anchor="middle">100% PNG Owned and Made</text>
  </g>

  <text class="chalk-word good-kai" x="130" y="270" text-anchor="middle" transform="rotate(90 130 270)">Good Kai</text>
  <text class="origin-side" x="720" y="284" text-anchor="middle" transform="rotate(-90 720 284)">100% PNG Owned and Made</text>

  <text class="chalk-word hamamas" x="424" y="490" text-anchor="middle">Hamamas</text>

  <text class="item-caption" x="438" y="559" text-anchor="middle">Adult Clam - For Meat Pie, Mash, Peas and Gravy</text>
</svg>
</body>
</html>
```